Business card design for Kovantrix

I need a business card based on the logo design produced for Kovantrix. The company is focused on triathlon and endurance sport coaching and the tag line is (per the logo) "Persistence. Strength. Performance". The design should be sophisticated, appropriate to an affluent and business oriented target market. Colors are optional but the color of the logo probably dictates the color used on the card. I envisage using the red logo, with black print for the wording and contact numbers on a white or cream background, but am open to alternative suggestions. I expect to select something fairly conventional, but would like to see some designs that are less conventional to stretch my thinking on what could be appropriate. I am assuming a single side design is best, but willing to consider double sided as an option.

Target Market(s)

Individual athletes and corporate health and wellness leaders

Industry/Entity Type

Health And Wellness

Contact Information for Business Card

The card should provide the following information:
Logo
My name: Marcus Bellingham
Company website: Kovantrix.com
My email: marcus.bellingham@kovantrix.com
My cell phone number: +1-555-812-6093

Font styles to use
Sans Serif

Colors

Designer to choose colors to be used in the design.

Requirements
Must have
• Space on the card - simple design, not over crowded.
Nice to have
• clean and clear font, nothing garish or mass market like
Should not have
• Do not add pictures

```html
<!DOCTYPE html>
<html lang="en">
<head>
<meta charset="utf-8">
<title>Kovantrix — Business Card</title>
<link rel="stylesheet" href="https://fonts.googleapis.com/css2?family=Lato:wght@400;700;900&display=swap">
<style>
  :root {
    --maroon: #7a1217;
    --maroon-light: #9a2a2f;
    --maroon-dark: #5e0b0f;
    --card-face: #f5f2ef;
    --ink: #1e1b1b;
    --page: #e6e3df;
  }
  html, body {
    margin: 0;
    padding: 0;
    width: 1200px;
    height: 970px;
    overflow: hidden;
    background: var(--page);
  }
  .business-card {
    position: absolute;
    left: 60px;
    top: 178px;
    width: 1080px;
    height: 615px;
    background: var(--card-face);
    box-shadow: 0 10px 30px rgba(0,0,0,0.18);
    overflow: hidden;
    font-family: "Lato", sans-serif;
  }
  .card-bands {
    position: absolute;
    inset: 0;
  }
  .brand-lockup {
    position: absolute;
    right: 60px;
    top: 150px;
    text-align: right;
  }
  .brand-name {
    margin: 0;
    font-weight: 900;
    font-size: 66px;
    line-height: 1;
    letter-spacing: -0.5px;
    color: var(--maroon);
  }
  .brand-tagline {
    margin: 8px 0 0;
    font-weight: 700;
    font-size: 22px;
    letter-spacing: -0.3px;
    color: var(--ink);
    text-transform: uppercase;
    white-space: nowrap;
  }
  .holder-name {
    position: absolute;
    left: 49px;
    top: 354px;
    margin: 0;
    font-weight: 700;
    font-size: 33px;
    color: var(--maroon);
  }
  .contact-list {
    position: absolute;
    left: 48px;
    top: 426px;
    margin: 0;
    padding: 0;
    list-style: none;
  }
  .contact-item {
    display: flex;
    align-items: center;
    height: 40px;
    font-size: 26px;
    color: var(--ink);
  }
  .contact-item + .contact-item { margin-top: 1px; }
  .contact-icon {
    width: 31px;
    height: 31px;
    margin-right: 14px;
    flex: none;
  }
</style>
</head>
<body>
  <section class="business-card">
    <svg class="card-bands" viewBox="0 0 1080 615" width="1080" height="615">
      <defs>
        <linearGradient id="band-top" x1="0" y1="0" x2="1" y2="1">
          <stop offset="0" stop-color="var(--maroon-light)"/>
          <stop offset="1" stop-color="var(--maroon)"/>
        </linearGradient>
        <linearGradient id="band-bottom" x1="0" y1="0" x2="1" y2="0">
          <stop offset="0" stop-color="var(--maroon-light)"/>
          <stop offset="1" stop-color="var(--maroon-dark)"/>
        </linearGradient>
      </defs>
      <path class="band-top" d="M0 0 H1080 V19 C950 8 820 6 700 18 C520 36 360 70 240 130 C150 175 60 215 0 244 Z" fill="url(#band-top)"/>
      <path class="band-bottom" d="M0 615 H1080 V371 C960 450 780 520 560 553 C380 578 180 582 0 587 Z" fill="url(#band-bottom)"/>
    </svg>

    <div class="brand-lockup">
      <h1 class="brand-name">Kovantrix</h1>
      <p class="brand-tagline">Persistence. Strength. Performance</p>
    </div>

    <h2 class="holder-name">Marcus Bellingham</h2>

    <ul class="contact-list">
      <li class="contact-item">
        <svg class="contact-icon" viewBox="0 0 32 32" aria-hidden="true">
          <circle cx="16" cy="16" r="14" fill="none" stroke="var(--maroon)" stroke-width="2"/>
          <path d="M11 9.5 L13.5 9 L15 13 L13.3 14.3 C14 16.5 15.5 18 17.7 18.7 L19 17 L23 18.5 L22.5 21 C21.8 22.5 19 23 16 21 C13 19 10.5 16 10.2 13 C10 11.5 10.3 10.2 11 9.5 Z" fill="var(--maroon)"/>
        </svg>
        <span>+1-555-812-6093</span>
      </li>
      <li class="contact-item">
        <svg class="contact-icon" viewBox="0 0 32 32" aria-hidden="true">
          <circle cx="16" cy="16" r="14" fill="none" stroke="var(--maroon)" stroke-width="2"/>
          <rect x="9" y="11" width="14" height="10" fill="var(--maroon)"/>
          <path d="M9 11 L16 17 L23 11" fill="none" stroke="var(--card-face)" stroke-width="1.4"/>
        </svg>
        <span>marcus.bellingham@kovantrix.com</span>
      </li>
      <li class="contact-item">
        <svg class="contact-icon" viewBox="0 0 32 32" aria-hidden="true">
          <circle cx="16" cy="16" r="14" fill="none" stroke="var(--maroon)" stroke-width="2"/>
          <circle cx="16" cy="16" r="9" fill="none" stroke="var(--maroon)" stroke-width="1.6"/>
          <ellipse cx="16" cy="16" rx="4" ry="9" fill="none" stroke="var(--maroon)" stroke-width="1.4"/>
          <path d="M7 16 H25 M8.5 11.5 H23.5 M8.5 20.5 H23.5" stroke="var(--maroon)" stroke-width="1.3"/>
        </svg>
        <span>Kovantrix.com</span>
      </li>
    </ul>
  </section>
</body>
</html>
```